Brightwave Reach - Business Card

We need a business card for a Social Media Marketing company that specializes in online marketing for small businesses in Canada using common Social Media platforms such as Pictora, Kinloop, Blinkit & Chirpo.

I have uploaded a copy of our logo which I would like utilized in the business card. We would like the business card to be modern yet classy design.

Our website is www.brightwavereach.ca

Industry/Entity Type

Marketing

Contact Information for Business Card

Email: info@brightwavereach.ca
Website: www.brightwavereach.ca
Telephone: 604-392-5108

Colors

Designer to choose colors to be used in the design.

Requirements
Must have
• Social Media icons on reverse
• Please add some designs with color.

```html
<!DOCTYPE html>
<html lang="en">
<head>
<meta charset="utf-8">
<title>Brightwave Reach – Business Card</title>
<link rel="stylesheet" href="https://fonts.googleapis.com/css2?family=Open+Sans:wght@400;700&display=swap">
<style>
  :root {
    --canvas: #d9dbdc;
    --card-dark: #262b2e;
    --card-light: #ffffff;
    --accent: #1ec3f2;
    --ink-light: #ffffff;
    --ink-dark: #262b2e;
  }
  * { margin: 0; padding: 0; box-sizing: border-box; }
  html, body {
    width: 1200px; height: 977px; overflow: hidden;
    background: var(--canvas);
    font-family: "Open Sans", Arial, sans-serif;
  }
  .canvas {
    position: relative; width: 1200px; height: 977px;
  }
  .card {
    position: absolute; left: 250px;
    width: 700px; height: 400px;
    overflow: hidden;
    box-shadow: 0 6px 18px rgba(0,0,0,0.18);
  }
  /* Reverse side */
  .card-back { top: 70px; background: var(--card-dark); color: var(--ink-light); }
  .card-back .brand {
    position: absolute; top: 120px; left: 0; width: 100%;
    display: flex; justify-content: center; align-items: center; gap: 14px;
  }
  .brand-mark {
    width: 22px; height: 22px; border: 3px solid currentColor;
  }
  .brand-name {
    font-weight: 700; font-size: 40px; letter-spacing: 1px;
    text-transform: uppercase; line-height: 1;
  }
  .social-row {
    position: absolute; top: 262px; left: 0; width: 100%;
    display: flex; justify-content: center; gap: 26px;
    list-style: none;
    font-size: 15px; font-weight: 700; letter-spacing: 0.3px;
  }
  /* Front side */
  .card-front { top: 507px; background: var(--card-light); }
  .card-front .shape { position: absolute; inset: 0; }
  .card-front .brand {
    position: absolute; top: 150px; left: 498px; width: 190px;
    color: var(--ink-dark);
    display: flex; flex-direction: column; align-items: center; gap: 10px;
  }
  .card-front .brand-name {
    font-size: 24px; letter-spacing: 0.5px;
    text-align: center; line-height: 1.1;
  }
  .card-front .brand-mark { width: 16px; height: 16px; }
  .contact {
    position: absolute; top: 222px; left: 74px;
    list-style: none; color: var(--ink-light);
    font-size: 17px; line-height: 1;
  }
  .contact li { display: flex; align-items: center; gap: 16px; margin-bottom: 13px; }
  .contact svg { width: 18px; height: 18px; fill: var(--accent); flex: none; }
</style>
</head>
<body>
<main class="canvas">

  <section class="card card-back" aria-label="Business card reverse">
    <div class="brand">
      <span class="brand-mark" aria-hidden="true"></span>
      <span class="brand-name">Brightwave Reach</span>
    </div>
    <ul class="social-row" aria-label="Social channels">
      <li>Linkwise</li>
      <li>Chirpo</li>
      <li>Vidloft</li>
      <li>Gleamr</li>
      <li>Pinora</li>
      <li>Kinloop</li>
    </ul>
  </section>

  <section class="card card-front" aria-label="Business card front">
    <svg class="shape" viewBox="0 0 700 400" preserveAspectRatio="none" aria-hidden="true">
      <path d="M0,0 L200,0 C420,40 520,230 395,400 L0,400 Z" fill="var(--card-dark)"/>
      <path d="M225,0 C450,45 545,235 418,400" fill="none" stroke="var(--accent)" stroke-width="8"/>
    </svg>

    <ul class="contact">
      <li>
        <svg viewBox="0 0 24 24"><path d="M6.6 10.8a15.1 15.1 0 0 0 6.6 6.6l2.2-2.2a1 1 0 0 1 1-.25 11.4 11.4 0 0 0 3.6.57 1 1 0 0 1 1 1V20a1 1 0 0 1-1 1A17 17 0 0 1 3 4a1 1 0 0 1 1-1h3.5a1 1 0 0 1 1 1c0 1.25.2 2.45.57 3.57a1 1 0 0 1-.25 1z"/></svg>
        <span>604-392-5108</span>
      </li>
      <li>
        <svg viewBox="0 0 24 24"><path d="M2 5h20v14H2z M2 5l10 8 10-8" /></svg>
        <span>info@brightwavereach.ca</span>
      </li>
      <li>
        <svg viewBox="0 0 24 24"><circle cx="12" cy="12" r="10"/><path d="M2 12h20M12 2v20" stroke="var(--card-dark)" stroke-width="1.6" fill="none"/><ellipse cx="12" cy="12" rx="4.5" ry="10" fill="none" stroke="var(--card-dark)" stroke-width="1.6"/></svg>
        <span>www.brightwavereach.ca</span>
      </li>
    </ul>

    <div class="brand">
      <span class="brand-name">Brightwave Reach</span>
      <span class="brand-mark" aria-hidden="true"></span>
    </div>
  </section>

</main>
</body>
</html>
```